Awesome new dental practice requires a New Letterhead design

We would like a new letterhead design to align with our new business branding & business cards. I have uploaded all the logos & current business card details that can be used. The new website can be viewed here https://lumaveo.com.au

Other useful details: Font Poppins
Colour Palettes:
Dark Pink #c45389
Light Pink: #e83e8c
Black

Please let me know if you have any questions or require anything else.

Industry/Entity Type

Dental

Font styles to use
Other font styles liked:
• Poppins

```html
<!DOCTYPE html>
<html lang="en">
<head>
<meta charset="UTF-8">
<title>Lumaveo Letterhead</title>
<link href="https://fonts.googleapis.com/css2?family=Poppins:wght@300;400;500;600;700&display=swap" rel="stylesheet">
<style>
:root{
  --pink-dark:#c45389;
  --pink-light:#e83e8c;
  --ink:#1b1b1f;
  --navy:#1c2350;
  --body-grey:#8d8f99;
  --link-blue:#4c7fb8;
  --paper:#ffffff;
  --backdrop:#e9e9eb;
}
*{margin:0;padding:0;box-sizing:border-box}
html,body{width:1200px;height:1200px;overflow:hidden;background:var(--backdrop);font-family:'Poppins',sans-serif}
.letterhead{position:absolute;left:204px;top:34px;width:792px;height:1132px;background:var(--paper);box-shadow:0 4px 18px rgba(0,0,0,.08);overflow:hidden}
.brand{position:absolute;left:62px;top:70px;font-size:40px;font-weight:600;color:var(--ink);letter-spacing:-1px;line-height:1}
.contact{position:absolute;right:70px;top:62px;font-size:12px;font-weight:500;color:var(--ink);line-height:1.55}
.contact-row{display:flex;align-items:flex-start;gap:10px}
.contact-row svg{flex:none;margin-top:3px}
.date{position:absolute;right:70px;top:176px;font-size:12px;font-weight:500;color:var(--ink)}
.date span{color:var(--pink-light)}
.recipient{position:absolute;left:62px;top:220px;font-size:12px;color:var(--ink);line-height:1.5}
.recipient .to{font-size:11px}
.recipient .name{font-size:17px;font-weight:600;color:var(--navy);line-height:1.3}
.recipient .label{color:var(--pink-light);font-weight:500}
.recipient a{color:var(--link-blue);text-decoration:none}
.body{position:absolute;left:62px;right:70px;top:380px;font-size:13px;line-height:1.7}
.body p{margin-bottom:26px}
.body .light{color:var(--body-grey);font-weight:300}
.body .strong{color:var(--ink);font-weight:500}
.signoff{position:absolute;left:62px;top:858px}
.signature{width:190px;height:46px;background:linear-gradient(90deg,#eceef3,#f4f5f8);border-radius:4px}
.signer{margin-top:8px;font-size:16px;color:var(--pink-light);letter-spacing:.5px}
.role{font-size:13px;font-weight:700;color:var(--navy);margin-top:2px}
.footer{position:absolute;left:0;bottom:0;width:792px;height:96px}
.tagline{position:absolute;right:34px;bottom:24px;font-size:15px;font-weight:500;color:#fff;white-space:nowrap;line-height:1.4}
.tagline b{color:var(--ink);font-weight:600}
</style>
</head>
<body>
<main class="letterhead">
  <div class="brand">lumaveo</div>

  <div class="contact">
    <div class="contact-row">
      <svg width="11" height="11" viewBox="0 0 24 24"><path fill="#e83e8c" d="M6.6 10.8a15 15 0 0 0 6.6 6.6l2.2-2.2a1 1 0 0 1 1-.25 11.4 11.4 0 0 0 3.6.57 1 1 0 0 1 1 1V20a1 1 0 0 1-1 1A17 17 0 0 1 3 4a1 1 0 0 1 1-1h3.5a1 1 0 0 1 1 1c0 1.250.2 2.45.57 3.6a1 1 0 0 1-.25 1z"/></svg>
      <span>(08) 9046 2185</span>
    </div>
    <div class="contact-row">
      <svg width="11" height="11" viewBox="0 0 24 24"><path fill="#e83e8c" d="M2 5h20v14H2z"/><path fill="none" stroke="#fff" stroke-width="2" d="M2 5l10 8 10-8"/></svg>
      <span>hello@lumaveo.com.au</span>
    </div>
    <div class="contact-row">
      <svg width="11" height="11" viewBox="0 0 24 24"><circle cx="12" cy="12" r="10" fill="#e83e8c"/><path fill="none" stroke="#fff" stroke-width="1.6" d="M2 12h20M12 2c3 3 3 17 0 20M12 2c-3 3-3 17 0 20"/></svg>
      <span>www.lumaveo.com.au</span>
    </div>
    <div class="contact-row">
      <span style="width:11px;flex:none"></span>
      <span>Shop 4, 27 Marlow Street,<br>Kestrel Bay, WA 6799</span>
    </div>
  </div>

  <div class="date"><span>Date:</span> 24-03-2018</div>

  <section class="recipient">
    <div class="to">To</div>
    <div class="name">Owen Hartley</div>
    <div>CEO, BRIGHTFORM STUDIO</div>
    <div><span class="label">A:</span> 45 Lake View Road, Pune, India 411001</div>
    <div><span class="label">P:</span> +91 90412 3365, +91 80557 21940</div>
    <div><span class="label">W:</span> <a href="#">www.brightformstudio.com</a></div>
  </section>

  <section class="body">
    <p class="light">Lorem ipsum dolor sit amet, consectetur adipiscing elit. Pellentesque dictum, ante non ullamcorp er convallis, nunc quam blandit metus, ac mollis eros felis a orci. Donec congue, mauris ut pulvinar lobortis, dolor massa feugiat nisi, at tincidunt metus leo vel elit. Proin facilisis semper lobortis.</p>
    <p class="strong">Nulla egestas vulputate risus, ut vestibulum diam commodo id. Mauris ornare libero eu erat porttitor ultrices. Proin sed lectus scelerisque ligula bibendum sagittis ac nec leo. Donec ac accumsan diam, et lobortis mauris.</p>
    <p class="light">Nulla congue volutpat nisl ac lobortis. Integer dignissim interdum libero, quis feugiat velit pretium at. Phasellus sit amet libero rutrum, feugiat odio et, tempus purus. Cras ultricies, leo at fringilla sollicitudin, leo sapien placerat enim, a rutrum lorem enim ut tortor. Phasellus magna ante, congue maximus egestas sit amet, venenatis scelerisque felis.</p>
    <p class="strong">Nulla congue volutpat nisl ac lobortis. Integer dignissim interdum libero, quis feugiat velit pretium at. Phasellus sit amet libero rutrum, feugiat odio et, tempus purus. Cras ultricies, leo at fringilla sollicitudin, leo sapien placerat enim, a rutrum lorem enim ut tortor. Phasellus magna ante, congue maximus egestas sit amet, venenatis scelerisque felis.</p>
  </section>

  <section class="signoff">
    <div class="signature" role="img" aria-label="Handwritten signature"></div>
    <div class="signer">CLARA WHITFIELD</div>
    <div class="role">CHAIRMAN</div>
  </section>

  <svg class="footer" viewBox="0 0 792 96" preserveAspectRatio="none">
    <path fill="#c45389" d="M0 82 L326 82 C348 82 350 74 352 56 C354 40 360 36 380 36 L792 36 L792 96 L0 96 Z"/>
  </svg>
  <div class="tagline">Life is short, <b>Smile</b> while you still have teeth</div>
</main>
</body>
</html>
```